TAVORINDS LLC

Looking to create a brand new website for my upcoming buisness. We offer training and provide support for horse owners in South florida. Our mission is to provide training for your equine family member to just not having enough time and needing your horse excercised. Got any ponies that your to big for, keeps throwing off your child and needs to be kid ready? We got you covered! We also provide horse care whether you are heading out of town or simply don’t have time. We can feed your horse, clean stalls, turnout, grooming, etc.
Open to any new and creative ideas for a website to jumpstart my equine buisness!

```html
<!DOCTYPE html>
<html lang="en">
<head>
<meta charset="utf-8">
<title>Tavorinds LLC</title>
<link href="https://fonts.googleapis.com/css2?family=Exo+2:wght@500;600;700&family=Lato:wght@400;700&display=swap" rel="stylesheet">
<style>
:root{
  --brown:#6b3f26;
  --brown-deep:#5a341f;
  --copper:#b8704a;
  --copper-light:#c98559;
  --peach:#e4bca5;
  --ink:#222;
  --text:#3a3a3a;
  --footer:#2a2a2a;
  --white:#fff;
}
*{margin:0;padding:0;box-sizing:border-box}
html,body{width:1200px;height:3232px;overflow:hidden}
body{position:relative;font-family:"Lato",sans-serif;color:var(--text);background:var(--white)}
.abs{position:absolute}
h1,h2,h3,.brand{font-family:"Exo 2",sans-serif}
.btn{position:absolute;display:flex;align-items:center;justify-content:center;border-radius:23px;background:linear-gradient(90deg,var(--copper-light),var(--copper) 60%,#9d5b39);color:var(--white);font-weight:700;font-size:15px}
.accent{color:var(--copper)}
.section-title{position:absolute;left:0;width:1200px;text-align:center;font-size:40px;font-weight:700;color:var(--brown)}
.lead{position:absolute;left:290px;width:620px;text-align:center;font-size:15px;line-height:28px;color:var(--ink)}

/* header */
.site-header{position:absolute;top:0;left:0;width:1200px;height:90px;background:var(--white)}
.site-header .brand{position:absolute;left:111px;top:22px;font-size:30px;font-weight:700;color:var(--brown)}
.nav a{position:absolute;top:33px;font-size:15px;color:var(--ink);text-decoration:none}
.nav .contact{left:948px;top:21px;width:140px;height:45px}

/* hero */
.hero{position:absolute;top:90px;left:0;width:1200px;height:520px;overflow:hidden;background:var(--brown)}
.hero-photo{position:absolute;left:480px;top:0;width:720px;height:520px;background:linear-gradient(90deg,var(--brown) 0%,#8a6046 30%,#b79277 55%,#cdb49a 80%,#a9b185 100%)}
.hero .kicker{position:absolute;left:111px;top:92px;font-family:"Exo 2",sans-serif;font-size:27px;font-weight:500;color:var(--white)}
.hero h1{position:absolute;left:111px;top:132px;font-size:51px;font-weight:700;color:var(--white)}
.hero p{position:absolute;left:111px;top:215px;width:500px;font-size:17px;line-height:29px;color:var(--white)}
.hero .btn{left:111px;top:305px;width:166px;height:45px}
.hero-curve{position:absolute;left:0;top:520px}

/* about */
.about-circle{position:absolute;left:270px;top:770px;width:260px;height:260px;border-radius:50%;background:var(--peach)}
.about-photo-a{position:absolute;left:111px;top:645px;width:366px;height:311px;border-radius:6px;background:linear-gradient(135deg,#6e2f1c,#a85a34 45%,#c98a5f 70%,#3f4a3a)}
.about-photo-b{position:absolute;left:234px;top:964px;width:317px;height:197px;border-radius:4px;background:linear-gradient(180deg,#b9cbe0 0%,#dfe8ef 45%,#5c7a45 70%,#8c5a35 100%)}
.about h2{position:absolute;left:621px;top:685px;font-size:40px;font-weight:700;color:var(--brown)}
.about .intro{position:absolute;left:621px;top:754px;width:467px;font-size:15px;line-height:28px;color:var(--ink);text-align:justify}
.about .body{position:absolute;left:621px;top:827px;width:467px;font-size:14.5px;line-height:28.5px;color:var(--text);text-align:justify}
.about .btn{left:621px;top:1065px;width:140px;height:45px}

/* mission */
.mission{position:absolute;left:0;top:1251px;width:1200px;height:349px;background:linear-gradient(90deg,rgba(108,64,38,.95),rgba(120,76,48,.9) 50%,rgba(108,64,38,.95)),linear-gradient(180deg,#7c5238,#5e3820)}
.mission h2{position:absolute;left:0;top:55px;width:1200px;text-align:center;font-size:40px;font-weight:700;color:var(--white)}
.mission .icon{position:absolute;left:574px;top:130px}
.mission p{position:absolute;left:200px;top:206px;width:800px;text-align:center;font-size:22px;line-height:36px;color:var(--white)}

/* services */
.service-card{position:absolute;top:1841px;width:452px;height:298px;border-radius:6px;box-shadow:6px 6px 0 var(--copper);overflow:hidden}
.service-card .media{position:absolute;inset:0}
.care .media{background:radial-gradient(circle at 60% 45%,#8a4a2c 0%,#4a2a1c 35%,#1f2a1c 70%)}
.training .media{background:radial-gradient(circle at 55% 55%,#a8652f 0%,#5a6a2c 40%,#24361a 80%)}
.service-card .shade{position:absolute;left:0;bottom:0;width:100%;height:120px;background:linear-gradient(180deg,transparent,rgba(0,0,0,.45))}
.service-card h3{position:absolute;left:0;bottom:42px;width:100%;text-align:center;font-size:22px;font-weight:500;color:var(--white)}

/* contact */
.contact-bg{position:absolute;left:0;top:2200px;width:1200px;height:740px;background:linear-gradient(180deg,#fff 0%,#f6f1ee 100%)}
.field{position:absolute;height:58px;background:var(--white);border:1px solid #ece6e2;border-radius:4px;box-shadow:0 3px 6px rgba(0,0,0,.07);font-size:16px;color:#333;padding:19px 0 0 28px}
.field.message{height:108px;padding-top:20px}
.contact-form .btn{left:531px;top:2737px;width:139px;height:45px}

/* footer */
.footer{position:absolute;left:0;top:2925px;width:1200px;height:307px;background:var(--footer);color:var(--white)}
.footer .brand{position:absolute;left:111px;top:14px;font-size:31px;font-weight:700}
.footer .tagline{position:absolute;left:115px;top:62px;width:320px;font-size:16.5px;line-height:30.5px}
.social{position:absolute;top:166px;width:45px;height:45px;border-radius:50%;border:1.5px solid var(--copper)}
.footer h4{position:absolute;top:25px;font-family:"Exo 2",sans-serif;font-size:16px;font-weight:700}
.links{position:absolute;top:66px;list-style:none}
.links li{height:30px;font-size:16.5px;display:flex;align-items:center;gap:12px}
.chev{color:var(--copper);font-size:14px}
.contact-info{position:absolute;left:898px;top:66px;list-style:none;font-size:15px;line-height:25px}
.contact-info li{position:relative;padding-left:26px;margin-bottom:10px}
.contact-info svg{position:absolute;left:0;top:5px}
.footer .rule{position:absolute;left:111px;top:245px;width:978px;height:1px;background:#444}
.footer .copy{position:absolute;left:0;top:268px;width:1200px;text-align:center;font-size:17px}
</style>
</head>
<body>

<header class="site-header">
  <div class="brand">TAVORINDS LLC</div>
  <nav class="nav">
    <a style="left:685px">Home</a>
    <a style="left:759px">About</a>
    <a style="left:834px">Services</a>
    <a class="btn contact">Contact Us</a>
  </nav>
</header>

<section class="hero">
  <div class="hero-photo" role="img" aria-label="Smiling young woman gently stroking a paint horse's face outside a stable"></div>
  <div class="abs" style="left:0;top:0;width:900px;height:520px;background:linear-gradient(90deg,var(--brown) 45%,rgba(107,63,38,0) 100%)"></div>
  <div class="kicker">WELCOME TO</div>
  <h1>TAVORINDS LLC</h1>
  <p>Lorem ipsum dolor sit amet, consectetur adipiscing elit, sed do eiusmod tempor incididunt ut labore et dolore magna aliqua.</p>
  <a class="btn">Request Quote</a>
</section>
<svg class="hero-curve" width="1200" height="100" viewBox="0 0 1200 100" style="top:530px">
  <path d="M0 78 Q600 -20 1200 78 L1200 100 L0 100 Z" fill="#fff"/>
  <path d="M0 78 Q600 -20 1200 78 L1200 72 Q600 -32 0 72 Z" fill="var(--copper)"/>
  <path d="M0 78 Q600 -10 1200 78 L1200 100 L0 100 Z" fill="#fff"/>
</svg>

<section class="about">
  <div class="about-circle"></div>
  <div class="about-photo-a" role="img" aria-label="Woman grooming a chestnut horse in a stable aisle"></div>
  <div class="about-photo-b" role="img" aria-label="Rider in helmet on a chestnut horse in an open field"></div>
  <h2>ABOUT <span class="accent">US</span></h2>
  <p class="intro">Lorem ipsum dolor sit amet, consectetur adipiscing elit, sed do eiusmod tempor incididunt ut labore et dolore.</p>
  <p class="body">Sed ut perspiciatis unde omnis iste natus error sit voluptatem accusantium doloremque laudantium, totam rem aperiam, eaque ipsa quae ab illo inventore veritatis et quasi architecto beatae vitae dicta sunt explicabo. Nemo enim ipsam voluptatem quia voluptas sit aspernatur aut odit aut fugit, sed quia consequuntur magni dolores eos qui ratione voluptatem sequi nesciunt. Neque porro quisquam est, qui dolorem ipsum quia dolor sit amet, consectetur, adipisci velit.</p>
  <a class="btn">Learn More</a>
</section>

<section class="mission" role="img" aria-label="Trainer lunging a horse in an arena, tinted brown">
  <h2>OUR <span class="accent">MISSION</span></h2>
  <svg class="icon" width="52" height="52" viewBox="0 0 52 52" fill="none" stroke="#fff" stroke-width="3" stroke-linecap="round">
    <circle cx="33" cy="32" r="14" fill="var(--copper)" stroke="none"/>
    <path d="M44 22 A21 21 0 1 1 30 5"/>
    <path d="M37 24 A13 13 0 1 1 30 13"/>
    <circle cx="24" cy="27" r="4"/>
    <path d="M24 27 L42 9 M38 5 L38 13 L46 13"/>
  </svg>
  <p>Our mission is to provide training for your equine family member to just not having enough time and needing your horse excercised.</p>
</section>

<section class="services">
  <h2 class="section-title" style="top:1663px">OUR <span class="accent">SERVICES</span></h2>
  <p class="lead" style="top:1733px">Lorem ipsum dolor sit amet, consectetur adipiscing elit, sed do eiusmod tempor incididunt ut labore et dolore.</p>
  <article class="service-card care" style="left:130px">
    <div class="media" role="img" aria-label="Chestnut horse being rinsed with a hose spray"></div>
    <div class="shade"></div>
    <h3>Horse Care</h3>
  </article>
  <article class="service-card training" style="left:619px">
    <div class="media" role="img" aria-label="Young rider on a chestnut horse in a sunlit forest arena"></div>
    <div class="shade"></div>
    <h3>Horse Training</h3>
  </article>
</section>

<div class="contact-bg"></div>
<section class="contact-form">
  <h2 class="section-title" style="top:2281px">REACH OUT <span class="accent">TO US TODAY!</span></h2>
  <p class="lead" style="top:2350px">Lorem ipsum dolor sit amet, consectetur adipiscing elit, sed do eiusmod tempor incididunt ut labore et dolore.</p>
  <div class="field" style="left:248px;top:2432px;width:345px">Name</div>
  <div class="field" style="left:607px;top:2432px;width:345px">Email ID</div>
  <div class="field" style="left:248px;top:2510px;width:345px">Area Code</div>
  <div class="field" style="left:607px;top:2510px;width:345px">Phone</div>
  <div class="field message" style="left:248px;top:2590px;width:704px">Message</div>
  <a class="btn">Submit</a>
</section>

<svg class="abs" style="left:0;top:2840px" width="1200" height="90" viewBox="0 0 1200 90">
  <path d="M0 88 Q600 -40 1200 88 L1200 90 L0 90 Z" fill="var(--copper)"/>
  <path d="M0 90 Q600 -20 1200 90 Z" fill="#fff"/>
  <path d="M0 90 Q600 -8 1200 90 Z" fill="var(--footer)"/>
</svg>
<footer class="footer">
  <div class="brand">TAVORINDS LLC</div>
  <p class="tagline">We provide a healthy environment uniquely suited to support your growth and healing.</p>
  <span class="social" style="left:113px" aria-label="Social profile"></span>
  <span class="social" style="left:177px" aria-label="Social profile"></span>

  <h4 style="left:497px">QUICK LINKS</h4>
  <ul class="links" style="left:497px">
    <li><span class="chev">»</span>Home</li>
    <li><span class="chev">»</span>About</li>
    <li><span class="chev">»</span>Services</li>
  </ul>
  <h4 style="left:704px">QUICK LINKS</h4>
  <ul class="links" style="left:704px">
    <li><span class="chev">»</span>Contact</li>
    <li><span class="chev">»</span>Privacy</li>
    <li><span class="chev">»</span>Terms</li>
  </ul>
  <h4 style="left:898px">CONTACT</h4>
  <ul class="contact-info">
    <li><svg width="12" height="15" viewBox="0 0 12 15"><path d="M6 0a6 6 0 0 0-6 6c0 4 6 9 6 9s6-5 6-9a6 6 0 0 0-6-6z" fill="var(--copper)"/><circle cx="6" cy="6" r="2.2" fill="var(--footer)"/></svg>Tavorinds LLC,<br>Address Comes Here</li>
    <li><svg width="13" height="13" viewBox="0 0 13 13"><path d="M3 0l2 3-1.5 1.5a8 8 0 0 0 5 5L10 8l3 2-1.5 3C5 13 0 8 0 1.5z" fill="var(--copper)"/></svg>+1 555-014-2288</li>
    <li style="margin-top:18px"><svg width="14" height="11" viewBox="0 0 14 11"><rect width="14" height="11" rx="1" fill="var(--copper)"/><path d="M0 1l7 5 7-5" stroke="var(--footer)" stroke-width="1.4" fill="none"/></svg>info@tavorindsllc.com</li>
  </ul>
  <div class="rule"></div>
  <p class="copy">2022 Tavorinds LLC. All Rights Reserved.</p>
</footer>

</body>
</html>
```